Horizontal scrolling homepage | ||
Consulting company needing a unique layout | ||
Consulting | ||
Qorvinex does consulting and implementation projects within CRM which are the processes around sales, marketing, service, call centers, web shops and more. Even though such engagements of course need the technical involvement from IT, it for sure also needs the business and in this segment the business consists of extrovert colorful people. |
The homepage must be different than the competitors and one way of doing that is by having horizontal scrolling with a menu bar on the left (if the design would be better, you can place it on the top). If it can be done in a cool way, then the left menu bar could be a bit to the right of the left border so that the scrolling background is visible. The scrolling should accelerate and de-accelerate when moving to the part of the homepage that should be displayed. There should not be a scrollbar. Menu: Start (or logo) Packages Services Next Step Career About On the start page there should be a combined sign up for newsletter and contact form (like here: brimtala[dot]dk[slash]om-brimtala). (Title, first name, last name, e-mail, mobile phone number, checkbox for Newsletter sign up and a free text field). The homepage must be easy to extend with additional texts. There should be teasers on the start page that will navigate the user to a place on one of the subpages with more information. It could be interesting to have flipping boxes like in Window Mobile, where one side of the box has a teaser one-liner and when the mouse hovers over it flips and the solution is on the back and when clicked, the page scrolls to the place with more information. But I do not know how easy that will be to implement with HTML5. Inspire me. In addition add the content that normally is part of a start page. You will find logo and teasers as attachments. For additional text use dummy latin. |
Cutting-Edge Unique/Creative Flashy Professional Corporate Modern Elegant Service Oriented |
See logo | ||
Arial Verdana Trebuchet MS |
left side | ||
http://www.morvenquaily.co.uk/ | ||
http://www.pravessa.com/ | ||
http://tunbelfield.com/ | ||
The homepage should be compatible with Internet Explorer and Crome, it should be accessible from Android pads and phones and Apple Iphones and Ipads, but I assume that will all automatically be possible when HTML5 is used for the development. The homepage must be easy to extend with additional menu items / texts. |

```html
<!DOCTYPE html>
<html lang="en">
<head>
<meta charset="utf-8">
<title>Qorvinex — People and Processes</title>
<link href="https://fonts.googleapis.com/css2?family=Arimo:wght@400;700&display=swap" rel="stylesheet">
<style>
  :root {
    --brand-blue: #1f6fb2;
    --ink: #3b3b3b;
    --ink-soft: #7a7a7a;
    --panel: #ffffff;
    --footer-top: #54413a;
    --footer-bottom: #3d2e29;
    --footer-text: #b9a89f;
    --accent-orange: #e07b1f;
    --accent-yellow: #f2c200;
    --contact-green: #2f9a34;
  }
  * { box-sizing: border-box; margin: 0; padding: 0; }
  html, body { width: 1200px; height: 566px; overflow: hidden; }
  body {
    position: relative;
    font-family: "Arimo", Arial, sans-serif;
    color: var(--ink);
    background: #fff;
  }
  .site-header {
    position: absolute; left: 0; top: 0; width: 1200px; height: 72px;
    background: linear-gradient(#ffffff, #f1f1f1);
    border-bottom: 1px solid #dcdcdc;
  }
  .brand { position: absolute; left: 120px; top: 10px; display: flex; align-items: center; gap: 10px; }
  .brand-mark { width: 40px; height: 40px; border-radius: 50%; background: var(--brand-blue); }
  .brand-name { font-size: 34px; font-weight: 700; color: var(--brand-blue); line-height: 1; }
  .brand-tagline { font-size: 11px; letter-spacing: 1.5px; color: var(--brand-blue); margin-top: 3px; }
  .social { position: absolute; right: 148px; top: 12px; }
  .social-label { font-size: 10px; color: var(--ink-soft); }
  .social-name { font-size: 22px; font-weight: 700; color: var(--ink); line-height: 1.1; }

  .hero-photo {
    position: absolute; left: 0; top: 72px; width: 1200px; height: 348px;
    background: linear-gradient(90deg, #e9e9e7 0%, #d9d6d2 30%, #cfc6bd 55%, #dcc0a8 75%, #e7d8c8 100%);
  }

  .side-nav {
    position: absolute; z-index: 2; left: 120px; top: 84px; width: 204px; height: 352px;
    background: var(--panel); box-shadow: 0 2px 10px rgba(0,0,0,.3);
    padding-top: 8px;
  }
  .nav-item { position: relative; display: flex; align-items: center; height: 56px; padding-left: 14px; border-bottom: 1px solid #ececec; }
  .nav-item:last-child { border-bottom: 0; }
  .nav-icon { width: 34px; height: 34px; border-radius: 8px; margin-right: 14px; flex: none; }
  .nav-title { font-size: 18px; font-weight: 700; color: #555; line-height: 1; }
  .nav-sub { font-size: 10px; color: var(--ink-soft); margin-top: 3px; }
  .nav-item.is-active { background: linear-gradient(#ffffff, #eef3f8); }
  .nav-item.is-active .nav-title { color: var(--brand-blue); }
  .nav-item.is-active::after {
    content: ""; position: absolute; right: -14px; top: 14px;
    border-left: 14px solid #f4f6f9; border-top: 14px solid transparent; border-bottom: 14px solid transparent;
  }
  .icon-home { background: #4e8fd0; }
  .icon-packages { background: #e8b62a; }
  .icon-services { background: #d24a3c; }
  .icon-next { background: #3aa0c8; }
  .icon-careers { background: #7a8c99; }
  .icon-about { background: #5d9b3b; }

  .teaser {
    position: absolute; left: 348px; top: 163px; width: 384px; height: 185px;
    background: rgba(255,255,255,.78); border: 1px solid rgba(255,255,255,.9);
    padding: 16px 20px;
  }
  .teaser-lead { font-size: 19px; color: var(--brand-blue); white-space: nowrap; }
  .teaser-title { font-size: 24px; font-weight: 700; color: #333; margin-top: 6px; white-space: nowrap; }
  .teaser-text { font-size: 12.5px; color: #666; line-height: 1.45; margin-top: 10px; width: 330px; }
  .teaser-more { position: absolute; left: 20px; bottom: 18px; font-size: 13px; color: var(--accent-orange); }
  .teaser-more::before { content: "— "; }
  .teaser-dots { position: absolute; left: 292px; bottom: 22px; display: flex; gap: 4px; }
  .teaser-dots span { width: 11px; height: 11px; background: #fff; border: 1px solid #bbb; }
  .teaser-dots span.is-current { background: var(--accent-yellow); border-color: #c79d00; }
  .hero-next { position: absolute; left: 738px; top: 222px; }

  .contact-tab {
    position: absolute; left: 1168px; top: 148px; width: 32px; height: 136px;
    background: var(--contact-green); border-radius: 4px 0 0 4px;
    display: flex; align-items: center; justify-content: center;
  }
  .contact-tab span {
    transform: rotate(-90deg); white-space: nowrap;
    font-size: 13px; font-weight: 700; color: #fff; letter-spacing: .5px;
  }

  .site-footer {
    position: absolute; z-index: 1; left: 0; top: 420px; width: 1200px; height: 146px;
    background: linear-gradient(var(--footer-top), var(--footer-bottom));
    border-top: 1px solid #6d5a52;
  }
  .footer-links { position: absolute; left: 136px; top: 78px; display: flex; gap: 20px; list-style: none; }
  .footer-links li { font-size: 11px; color: var(--footer-text); }
  .copyright { position: absolute; left: 136px; top: 100px; font-size: 10px; color: #9b8a82; }
  .newsletter { position: absolute; left: 876px; top: 64px; }
  .newsletter-title { font-size: 12px; color: #d9ccc5; margin-left: 8px; }
  .newsletter-form { display: flex; gap: 6px; margin-top: 16px; }
  .newsletter-input {
    width: 146px; height: 30px; background: #2f2320; border: 1px solid #5e4b44;
    font-size: 10px; color: #7f6d66; padding: 9px 10px;
  }
  .newsletter-button {
    width: 66px; height: 30px; background: #5a453e; border: 1px solid #6f5a52;
    font-size: 10px; color: #e5d9d3; text-align: center; line-height: 28px;
  }
</style>
</head>
<body>
  <header class="site-header">
    <div class="brand">
      <div class="brand-mark"></div>
      <div>
        <div class="brand-name">Qorvinex</div>
        <div class="brand-tagline">PEOPLE AND PROCESSES</div>
      </div>
    </div>
    <div class="social">
      <div class="social-label">Find us on</div>
      <div class="social-name">Linkora</div>
    </div>
  </header>

  <div class="hero-photo" role="img" aria-label="Photo of smiling business professionals in an office"></div>

  <nav class="side-nav">
    <div class="nav-item is-active"><div class="nav-icon icon-home"></div><div><div class="nav-title">HOME</div><div class="nav-sub">start from here</div></div></div>
    <div class="nav-item"><div class="nav-icon icon-packages"></div><div><div class="nav-title">PACKAGES</div><div class="nav-sub">what we offers</div></div></div>
    <div class="nav-item"><div class="nav-icon icon-services"></div><div><div class="nav-title">SERVICES</div><div class="nav-sub">what we offers</div></div></div>
    <div class="nav-item"><div class="nav-icon icon-next"></div><div><div class="nav-title">NEXT STEP</div><div class="nav-sub">what we have shared</div></div></div>
    <div class="nav-item"><div class="nav-icon icon-careers"></div><div><div class="nav-title">CAREERS</div><div class="nav-sub">future with us</div></div></div>
    <div class="nav-item"><div class="nav-icon icon-about"></div><div><div class="nav-title">ABOUT US</div><div class="nav-sub">who we are</div></div></div>
  </nav>

  <section class="teaser">
    <p class="teaser-lead">Veltrix projects are big &amp; costly, Right?</p>
    <h1 class="teaser-title">Well, they don't have to be...</h1>
    <p class="teaser-text">Let's talk about how we can ensure that your Veltrix project costs are kept at a minimum.</p>
    <span class="teaser-more">read more</span>
    <div class="teaser-dots"><span class="is-current"></span><span></span><span></span><span></span></div>
  </section>

  <svg class="hero-next" width="22" height="56" viewBox="0 0 22 56" aria-hidden="true">
    <polyline points="3,3 19,28 3,53" fill="none" stroke="rgba(255,255,255,.75)" stroke-width="4"/>
  </svg>

  <div class="contact-tab"><span>CONTACT US</span></div>

  <footer class="site-footer">
    <ul class="footer-links">
      <li>Homepage</li><li>Packages</li><li>Services</li><li>Next Step</li><li>Career</li><li>About</li>
    </ul>
    <p class="copyright">Copyright 2012 Qorvinex. All Rights Reserved.</p>
    <div class="newsletter">
      <div class="newsletter-title">Newsletter Subscription</div>
      <div class="newsletter-form">
        <div class="newsletter-input">enter email address</div>
        <div class="newsletter-button">subscribe</div>
      </div>
    </div>
  </footer>
</body>
</html>
```